Student project platform needs an awareness flyer

Tornuvel is a matchmaking and crowdfunding site for student projects. On this platform, students can team up with each other to invent a new product, innovate, or start a business. They can also raise funds for their project.

** I am in need of an 8x11" flyer to print and distribute digitally which notifies students of all different skill sets that this site exists.

The flyer should communicate that a diverse user base is being built on this site, with people who have skills in programming, engineering, design, business, finance, and so on.

The flyer should also be clean and modern, with an emphasis on creativity and innovation. I've attached the business' logo to give you an idea of the artistic style we have already established.

Target Market(s)

University students

Industry/Entity Type

Crowdfunding

Font styles to use
Serif
Sans Serif

Requirements
Must have
• * Clean and modern design
• * Color scheme of my logo: #336699 and #669933 (blue and green)
• * Convey that this site is for people of different skill sets: programming, engineering, design, business, finance, and so on.
• * See the attached "Tornuvel Copy.txt" for text to include on the flyer

```html
<!DOCTYPE html>
<html lang="en">
<head>
<meta charset="utf-8">
<title>Tornuvel – Student Projects Flyer</title>
<link rel="stylesheet" href="https://fonts.googleapis.com/css2?family=Montserrat:wght@500;600;700;800&family=Oswald:wght@700&family=Roboto+Slab:wght@800&family=Roboto:wght@400;700&family=Varela+Round&display=swap">
<style>
  :root{
    --brand-blue:#336699;
    --brand-blue-deep:#1f5c9a;
    --brand-green:#669933;
    --brand-green-bright:#5f9b3a;
    --panel:#f1f2f4;
    --ink:#1c1c1c;
    --silver:#c9ccd1;
    --white:#ffffff;
    --social-red:#c23a2f;
  }
  *{margin:0;padding:0;box-sizing:border-box}
  html,body{width:960px;height:1200px;overflow:hidden;background:var(--panel)}
  .flyer{position:relative;width:960px;height:1200px;overflow:hidden;background:var(--panel);font-family:"Montserrat",sans-serif;color:var(--ink)}

  .hero-photo{position:absolute;left:0;top:0;width:960px;height:540px;
    background:radial-gradient(ellipse at 55% 45%,#d9b9a4 0%,#c8a48f 18%,#e7e3df 45%,#f4f3f1 75%),linear-gradient(90deg,#dcdad6,#f5f4f2 50%,#e4e2de)}
  .waves{position:absolute;left:0;top:0;width:960px;height:1200px}

  .join{position:absolute;left:104px;top:484px;font-weight:800;font-size:112px;line-height:1;color:var(--brand-green);letter-spacing:-2px;text-shadow:4px 5px 0 #2d3a22}
  .brand{position:absolute;left:104px;top:596px;width:300px;text-align:center}
  .brand-dot{width:76px;height:76px;border-radius:50%;background:var(--brand-blue);margin:0 auto 10px}
  .brand-name{font-weight:600;font-size:42px;line-height:48px;color:var(--brand-blue);letter-spacing:1px}

  .pitch{position:absolute;left:460px;top:598px;font-weight:500;font-size:30px;line-height:38px;color:var(--ink)}
  .pitch .hl-blue{color:var(--brand-blue-deep);font-weight:700}
  .pitch .hl-green{color:var(--brand-green);font-weight:600}
  .pitch .projects{display:block;font-family:"Roboto Slab",serif;font-weight:800;font-size:60px;line-height:72px;color:var(--brand-green);letter-spacing:1px}

  .skills{position:absolute;left:0;top:772px;width:960px;display:flex;justify-content:space-around;padding:0 60px;list-style:none}
  .skill{width:160px;text-align:center}
  .skill svg{width:60px;height:52px;display:block;margin:0 auto}
  .skill-rule{width:70px;height:2px;background:var(--brand-green);margin:8px auto 14px}
  .skill-label{font-weight:500;font-size:17px;letter-spacing:.3px}

  .about{position:absolute;left:88px;top:914px;width:316px}
  .about h2{font-weight:500;font-size:26px;color:var(--brand-green);margin-bottom:8px}
  .about h2 b{color:var(--brand-blue-deep);font-weight:700}
  .about p{font-family:"Roboto",sans-serif;font-size:16.5px;line-height:21px;text-align:justify}
  .about p b{color:var(--brand-blue-deep)}

  .callout{position:absolute;left:460px;top:910px}
  .callout h2{font-family:"Oswald",sans-serif;font-weight:700;font-size:42px;line-height:50px;color:var(--brand-blue-deep);letter-spacing:.5px}
  .callout h2 span{color:var(--brand-green)}
  .callout p{font-family:"Varela Round",sans-serif;font-size:30px;line-height:40px;color:var(--ink)}
  .callout p b{color:var(--brand-blue-deep);font-weight:400;-webkit-text-stroke:.7px var(--brand-blue-deep)}

  .social{position:absolute;left:160px;top:1148px;display:flex;gap:16px}
  .social span{width:30px;height:30px;border-radius:50%;background:var(--brand-blue)}
  .social span:last-child{background:var(--social-red)}
  .web{position:absolute;right:66px;top:1146px;font-weight:500;font-size:23px;color:var(--white)}
</style>
</head>
<body>
<main class="flyer">
  <div class="hero-photo" role="img" aria-label="Photo of four smiling university students standing together holding notebooks and folders in a bright hallway"></div>

  <svg class="waves" viewBox="0 0 960 1200" aria-hidden="true">
    <path d="M470 490 C650 465 820 420 960 392 L960 500 L470 500 Z" fill="var(--brand-green-bright)"/>
    <path d="M0 432 C300 420 520 570 960 520 L960 1200 L0 1200 Z" fill="var(--panel)"/>
    <path d="M0 386 C300 374 520 534 960 484 L960 520 C520 570 300 420 0 432 Z" fill="var(--brand-blue-deep)"/>
    <path d="M0 372 C300 360 520 520 960 470 L960 484 C520 534 300 374 0 386 Z" fill="var(--silver)"/>
    <path d="M0 1092 C350 1160 700 1110 960 1030 L960 1200 L0 1200 Z" fill="var(--white)"/>
    <path d="M0 1100 C350 1168 700 1118 960 1040 L960 1056 C700 1136 350 1184 0 1118 Z" fill="var(--brand-blue-deep)"/>
    <path d="M0 1118 C350 1184 700 1136 960 1056 L960 1200 L0 1200 Z" fill="var(--brand-green-bright)"/>
  </svg>

  <h1 class="join">JOIN</h1>
  <div class="brand">
    <div class="brand-dot"></div>
    <div class="brand-name">TORNUVEL</div>
  </div>

  <p class="pitch">TO <span class="hl-blue">SUPPORT</span> AND LEND<br>YOUR <span class="hl-green">SKILLS</span> TO <span class="hl-blue">STUDENT</span><span class="projects">PROJECTS!</span></p>

  <ul class="skills">
    <li class="skill">
      <svg viewBox="0 0 64 56" fill="none" stroke="var(--brand-blue)" stroke-width="3" stroke-linejoin="round"><rect x="6" y="4" width="52" height="36" rx="2"/><path d="M26 40 L24 50 H40 L38 40 M18 50 H46"/><path d="M24 16 L18 22 L24 28 M40 16 L46 22 L40 28 M35 14 L29 30"/></svg>
      <div class="skill-rule"></div><div class="skill-label">PROGRAMMING</div>
    </li>
    <li class="skill">
      <svg viewBox="0 0 64 56" fill="none" stroke="var(--brand-blue)" stroke-width="3" stroke-linejoin="round" stroke-linecap="round"><path d="M2 22 L14 12 L22 16 L32 12 L44 14 L52 10 L62 20 L50 34"/><path d="M14 12 L4 30 L10 36"/><path d="M32 12 L24 22 L30 26 L38 20 L50 34 L44 40"/><path d="M10 36 L16 30 L22 36 L16 42 Z M16 42 L22 36 L28 42 L22 48 Z M26 46 L32 40 L38 44 L32 50 Z"/></svg>
      <div class="skill-rule"></div><div class="skill-label">BUSINESS</div>
    </li>
    <li class="skill">
      <svg viewBox="0 0 64 56" fill="none" stroke="var(--brand-blue)" stroke-width="3" stroke-linejoin="round" stroke-linecap="round"><circle cx="32" cy="12" r="8"/><path d="M28 20 V24 H36 V20 M32 0 V2 M20 4 L22 6 M44 4 L42 6"/><rect x="18" y="26" width="28" height="18" rx="3"/><circle cx="26" cy="35" r="3"/><circle cx="38" cy="35" r="3"/><path d="M18 32 H10 V42 M46 32 H54 V42 M24 44 V52 M40 44 V52"/></svg>
      <div class="skill-rule"></div><div class="skill-label">ENGINEERING</div>
    </li>
    <li class="skill">
      <svg viewBox="0 0 64 56" fill="none" stroke="var(--brand-blue)" stroke-width="3" stroke-linejoin="round" stroke-linecap="round"><rect x="6" y="8" width="52" height="32" rx="2"/><path d="M26 40 L24 50 H40 L38 40 M18 50 H46"/><path d="M20 32 L24 26 L52 2 L56 6 L30 30 Z"/><path d="M16 34 C18 30 22 30 22 32"/></svg>
      <div class="skill-rule"></div><div class="skill-label">DESIGN</div>
    </li>
    <li class="skill">
      <svg viewBox="0 0 64 56" fill="none" stroke="var(--brand-blue)" stroke-width="3" stroke-linejoin="round"><rect x="6" y="4" width="52" height="36" rx="2"/><path d="M26 40 L24 50 H40 L38 40 M18 50 H46"/><circle cx="30" cy="23" r="11"/><path d="M30 23 V12 M30 23 L40 28"/><path d="M34 10 A11 11 0 0 1 44 20 L34 20 Z" fill="var(--brand-blue)"/></svg>
      <div class="skill-rule"></div><div class="skill-label">FINANCE</div>
    </li>
  </ul>

  <section class="about">
    <h2>WHAT IS <b>TORNUVEL?</b></h2>
    <p>Tornuvel is a matchmaking and crowdfunding platform for student projects. It allows students to form teams of diverse skills and raise money to build, <b>innovate, invent, or start a business.</b></p>
  </section>

  <section class="callout">
    <h2><span>CALLING</span> ALL STUDENTS</h2>
    <p>Who want to <b>Build,</b><br><b>Innovate, Invent,</b> or<br><b>Start a Business.</b></p>
  </section>

  <div class="social" aria-label="Social media links"><span></span><span></span><span></span></div>
  <div class="web">www.tornuvel.com</div>
</main>
</body>
</html>
```